Design professional label for greener chemicals (cleaning and lubrication) brand

Design a b2b professional label that is based on the examples given.
Size: 135 x 200 mm, please use text of the label description doc (only the kaltro stainless steel polish example design document has the right text and size)
It should include:
1. Logo, can be fully changed except the shape of "KALTRO", colors and fonts of the rest can be customized
2. Focus should be on professional market, we would like to express the professionalism and high quality of the product
3. Focus should be on our brand name "KALTRO BRIGHTER COMPOUNDS"
4. Should include product name, product description, danger sentences, danger symbol, user instructions, image
5. Should include numbers that explain what the product does: 1. Prewash 2. Clean 3. Protect 4. Preserve and highlight number 2.

Target Market(s)

Professional cleaning companies, steel industry, food industry, pharmacy industry

Industry/Entity Type

Cleaning industry, steel industry, food industry, boat cleaning, car cleaning, professional lubrication

Font styles to use
Sans Serif

Requirements
Must have
• Professional look, clean look, image, focus on our brand name
Nice to have
• Numbers (see explanation), label divided in three parts (logo and product name and image in the middle as the highlight)

```html
<!DOCTYPE html>
<html lang="en">
<head>
<meta charset="utf-8">
<title>Kaltro Stainless Steel Polish – Label</title>
<link rel="stylesheet" href="https://fonts.googleapis.com/css2?family=Russo+One&family=Montserrat:wght@400;500&family=Oxanium:wght@500;700&display=swap">
<style>
  :root{
    --bg:#000000;
    --brand-blue:#1e3f9e;
    --brand-green:#7dbb3a;
    --band-green:#8db33f;
    --steel-light:#e4e6e8;
    --steel-mid:#b9bdc1;
    --steel-dark:#6f7479;
    --white:#ffffff;
    --danger-red:#e01e25;
  }
  *{box-sizing:border-box;margin:0;padding:0}
  html,body{width:1200px;height:1200px;overflow:hidden;background:var(--bg)}
  .label{position:absolute;left:30px;top:215px;width:1140px;height:771px;overflow:hidden}
  .label-photo{position:absolute;inset:0;
    background:
      linear-gradient(180deg,rgba(0,0,0,0) 55%,rgba(170,205,70,.85) 82%,rgba(141,179,63,1) 92%),
      linear-gradient(100deg,var(--steel-mid) 0%,var(--steel-light) 30%,#cfd2d5 55%,var(--steel-dark) 80%,#9a9fa4 100%);}
  .bottom-band{position:absolute;left:0;right:0;top:702px;bottom:0;background:var(--band-green)}
  .web-line{position:absolute;top:725px;left:0;right:0;font:700 17px "Oxanium",sans-serif;color:var(--white);white-space:nowrap}
  .web-line .email{position:absolute;left:340px}
  .web-line .site{position:absolute;left:630px}
  .web-line svg{position:absolute;left:602px;top:2px}

  /* left panel */
  .use-title{position:absolute;left:100px;top:44px;font:700 7px "Oxanium",sans-serif;color:var(--white)}
  .use-icon{position:absolute;left:78px;width:82px;height:82px;border:3px solid var(--white);border-radius:16px;
    background:rgba(255,255,255,.18);box-shadow:0 0 0 2px rgba(120,120,120,.4)}
  .use-caption{position:absolute;left:60px;width:118px;text-align:center;font:700 6px/1.3 "Oxanium",sans-serif;color:var(--white)}
  .field{position:absolute;left:36px;font:700 12px/14px "Oxanium",sans-serif;color:var(--brand-blue)}
  .field-line{position:absolute;left:36px;width:162px;border-top:1px solid var(--brand-blue)}
  .company{position:absolute;left:36px;top:590px;font:700 8.6px/12.3px "Oxanium",sans-serif;color:var(--brand-blue);white-space:nowrap}
  .label-number{position:absolute;left:36px;top:672px;font:700 14px/16px "Oxanium",sans-serif;color:var(--brand-blue)}

  /* centre panel */
  .brand-name{position:absolute;left:450px;top:62px;width:254px;text-align:center;font:400 74px/1 "Russo One",sans-serif;color:var(--brand-blue)}
  .product-kicker{position:absolute;left:400px;width:340px;top:246px;text-align:center;font:400 31px/1 "Russo One",sans-serif;color:var(--brand-blue)}
  .product-name{position:absolute;left:380px;width:385px;top:276px;text-align:center;font:400 116px/1 "Russo One",sans-serif;
    color:var(--steel-light);-webkit-text-stroke:4px var(--brand-blue)}
  .tagline{position:absolute;left:400px;width:340px;top:421px;text-align:center;font:700 15px "Oxanium",sans-serif;color:var(--brand-blue);
    padding-bottom:6px;border-bottom:1px solid var(--brand-blue)}
  .eco-badge{position:absolute;left:709px;top:483px}
  .brand-banner{position:absolute;left:431px;top:617px;width:300px;height:38px;background:var(--brand-blue);transform:skewX(-14deg)}
  .brand-banner span{display:block;transform:skewX(14deg);text-align:center;font:italic 500 18px/38px "Montserrat",sans-serif;color:var(--white);letter-spacing:.5px}
  .banner-stripes{position:absolute;left:737px;top:617px}

  /* right panel */
  .info{position:absolute;left:883px;width:240px;color:var(--white);font:400 12.4px/16px "Montserrat",sans-serif}
  .info h2{font:700 12px "Oxanium",sans-serif;margin-bottom:2px}
  .info ul{list-style:none;margin-top:14px}
  .info li{padding-left:8px;text-indent:-8px}
  .hazard{position:absolute;left:888px;top:469px;width:225px;height:129px;background:var(--white);padding:12px 6px 0}
  .pictograms{display:flex;gap:8px;margin-bottom:10px}
  .pictogram{width:48px;height:48px;border:4px solid var(--danger-red);display:flex;align-items:center;justify-content:center;
    font:700 34px "Montserrat",sans-serif;color:#000}
  .hazard p{font:700 5.4px/7px "Oxanium",sans-serif;color:var(--danger-red)}
</style>
</head>
<body>
<main class="label">
  <div class="label-photo" role="img" aria-label="Photograph of a stainless steel professional kitchen with counter, sink and drawers, fading to green at the bottom"></div>
  <div class="bottom-band"></div>
  <div class="web-line">
    <span class="email">info@kaltrocompounds.com</span>
    <svg width="20" height="20" viewBox="0 0 20 20" fill="none" stroke="#fff" stroke-width="1.5"><circle cx="10" cy="10" r="8"/><ellipse cx="10" cy="10" rx="3.5" ry="8"/><path d="M2 10h16M3.5 6h13M3.5 14h13"/></svg>
    <span class="site">www.kaltrocompounds.com</span>
  </div>

  <section class="panel-left">
    <div class="use-title">USE ON/FOR:</div>
    <div class="use-icon" style="top:72px" role="img" aria-label="Icon of stainless steel kitchen equipment"></div>
    <div class="use-caption" style="top:159px">STAINLESS<br>STEEL KITCHENS</div>
    <div class="use-icon" style="top:194px" role="img" aria-label="Icon of a sailing boat"></div>
    <div class="use-caption" style="top:283px">BOATS</div>
    <div class="use-icon" style="top:313px" role="img" aria-label="Icon of industrial gears"></div>
    <div class="use-caption" style="top:398px">INDUSTRIAL<br>STEEL SURFACES</div>

    <div class="field" style="top:436px">Expiring dates:</div>
    <div class="field-line" style="top:469px"></div>
    <div class="field" style="top:484px">Batch number:</div>
    <div class="field-line" style="top:517px"></div>
    <div class="field" style="top:532px">Net volume:</div>
    <div class="field-line" style="top:565px"></div>

    <div class="company">
      Company information:<br>
      Produced by Kaltro Laboratories Int. B.V.<br>
      Postbus 4417 - 5200 AB Harlen (NL)<br>
      Phone NL: +31 410 72 19 00<br>
      Lindenlaan 48 bus 12 – 3600 Brevel (B)<br>
      Phone B: +32 13 48 27 00
    </div>
    <div class="label-number">Label number: 23092021</div>
  </section>

  <section class="panel-centre">
    <div class="brand-name">KALTRO</div>
    <div class="product-kicker">STAINLESS STEEL</div>
    <div class="product-name">POLISH</div>
    <div class="tagline">RESTORE STEEL SURFACES HOLOGRAM FREE</div>
    <svg class="eco-badge" width="92" height="92" viewBox="0 0 92 92" role="img" aria-label="Eco badge">
      <circle cx="46" cy="46" r="42" fill="none" stroke="var(--brand-blue)" stroke-width="5"/>
    </svg>
    <div class="brand-banner"><span>BRIGHTER COMPOUNDS</span></div>
    <svg class="banner-stripes" width="26" height="38" viewBox="0 0 26 38">
      <path d="M0 0h4l8 38h-4z M9 0h4l8 38h-4z" fill="var(--brand-blue)"/>
    </svg>
  </section>

  <section class="panel-right">
    <div class="info" style="top:86px">
      <h2>Product description:</h2>
      Lustrel is a mildly abrasive cleansing cream with preservative properties. For removing stubborn dirt, water stains and deposits on stainless steel with a hologram free finish. Lustrel is non-tox and safe to use.
    </div>
    <div class="info" style="top:226px">
      <h2>User instructions:</h2>
      <ul>
        <li>- Shake before use.</li>
        <li>- Apply with a damp brush, sponge or pad.</li>
        <li>- Adjust rubbing pressure and duration to the persistence of the soiling.</li>
        <li>- Add water as needed while rubbing, rub in the direction of the structure.</li>
        <li>- Rinse with clean water.</li>
      </ul>
    </div>
    <div class="hazard">
      <div class="pictograms">
        <div class="pictogram" role="img" aria-label="Hazard pictogram: acute toxicity"></div>
        <div class="pictogram" role="img" aria-label="Hazard pictogram: flammable"></div>
        <div class="pictogram" aria-label="Hazard pictogram: irritant">!</div>
        <div class="pictogram" role="img" aria-label="Hazard pictogram: health hazard"></div>
      </div>
      <p>Danger: Causes severe skin burns and eye damage. Wear protective gloves, protective clothing, eye protection, face protection.<br>
      IF SWALLOWED: rinse mouth — DO NOT induce vomiting. Immediately call a POISON CENTER, a physician.<br>
      IF ON SKIN (or hair): Take off immediately all contaminated clothing.</p>
    </div>
  </section>
</main>
</body>
</html>
```